Pike Hauling Business Card Design Project

We need a new company business card. We provide professional timber harvesting (logging) and forest management services. I'm open to any creative design. Most company caps and shirts are navy blue and Light grey. Logo does not necessarily have to contain those colors. Logo containing picture of logging equipment, log truck, trees, or logs are acceptable. Be creative. Final logo should communicate our company's pride and professionalism in the East Texas Timber Industry.
Updates

Target Market(s)

Timber owners, sawmills, and forestry professionals

Industry/Entity Type

Business

Requirements
Must have
• Must have Contact Info.
Phone: 936-402-5187
address: PO Box 8412
Cedar Bend, Tx 77390
www.rbpikehauling.example
rbpikehauling@mailbox.example
Owner: Ross Pike

Or design must leave room for this info.

```html
<!DOCTYPE html>
<html lang="en">
<head>
<meta charset="utf-8">
<title>R.B. Pike Hauling Company – Business Card</title>
<link rel="stylesheet" href="https://fonts.googleapis.com/css2?family=Open+Sans:wght@400;600&display=swap">
<style>
  :root {
    --stage: #e4e4e4;
    --paper: #f6f6f4;
    --leaf: #8fb84a;
    --leaf-soft: #c9dea5;
    --bark: #3e1f13;
    --bark-dark: #2a140c;
    --ink: #1b1b1b;
    --white: #ffffff;
  }
  * { margin: 0; padding: 0; box-sizing: border-box; }
  html, body {
    width: 1200px; height: 864px; overflow: hidden;
    background: var(--stage);
    font-family: "Open Sans", Arial, sans-serif;
  }
  .card {
    position: absolute; left: 290px;
    width: 620px; height: 354px;
    background: var(--paper);
    box-shadow: 0 6px 18px rgba(0,0,0,0.18);
    overflow: hidden;
  }
  .card--front { top: 48px; }
  .card--back { top: 462px; }
  .card__art { position: absolute; inset: 0; width: 620px; height: 354px; }

  .front__brand {
    position: absolute; right: 40px; top: 216px;
    text-align: right; color: var(--ink);
    font-size: 28px; font-weight: 400; line-height: 32px;
    letter-spacing: 0.5px; text-transform: uppercase;
  }
  .front__web {
    position: absolute; right: 66px; top: 290px;
    color: var(--white); font-size: 15px; font-weight: 400;
  }

  .back__brand {
    position: absolute; left: 36px; top: 34px;
    text-align: center; color: var(--leaf);
    font-size: 28px; font-weight: 400; line-height: 32px;
    letter-spacing: 0.5px; text-transform: uppercase;
  }
  .back__contact {
    position: absolute; right: 30px; top: 180px;
    text-align: right; color: var(--white);
  }
  .back__name { font-size: 22px; font-weight: 600; letter-spacing: 0.5px; text-transform: uppercase; line-height: 26px; }
  .back__role { font-size: 12px; font-weight: 600; color: var(--leaf); margin-bottom: 8px; }
  .back__list { list-style: none; font-size: 14px; line-height: 22px; }
  .back__list li { display: flex; justify-content: flex-end; align-items: center; gap: 8px; white-space: nowrap; }
  .icon { width: 12px; height: 12px; fill: var(--leaf); flex: none; }
</style>
</head>
<body>

<section class="card card--front">
  <svg class="card__art" viewBox="0 0 620 354">
    <defs>
      <linearGradient id="treeTone" x1="0" y1="0" x2="0" y2="1">
        <stop offset="0" stop-color="#dfeccb"/>
        <stop offset="1" stop-color="var(--leaf-soft)"/>
      </linearGradient>
    </defs>
    <polygon points="40,12 420,12 420,150 90,336 40,336" fill="url(#treeTone)" role="img" aria-label="Illustration of a row of bare green trees"/>
    <line x1="66" y1="354" x2="620" y2="66" stroke="var(--ink)" stroke-width="2"/>
    <polygon points="90,354 620,80 620,354" fill="var(--leaf)"/>
  </svg>
  <h1 class="front__brand">R.B. Pike<br>Hauling Company</h1>
  <p class="front__web">www.rbpikehauling.example</p>
</section>

<section class="card card--back">
  <svg class="card__art" viewBox="0 0 620 354">
    <defs>
      <linearGradient id="barkTone" x1="0" y1="1" x2="1" y2="0">
        <stop offset="0" stop-color="var(--bark)"/>
        <stop offset="1" stop-color="var(--bark-dark)"/>
      </linearGradient>
    </defs>
    <line x1="0" y1="286" x2="620" y2="0" stroke="var(--leaf)" stroke-width="2"/>
    <polygon points="0,302 620,14 620,354 0,354" fill="url(#barkTone)"/>
  </svg>
  <h2 class="back__brand">R.B. Pike<br>Hauling Company</h2>
  <div class="back__contact">
    <p class="back__name">Ross Pike</p>
    <p class="back__role">Owner</p>
    <ul class="back__list">
      <li>936-402-5187
        <svg class="icon" viewBox="0 0 12 12"><path d="M2.5 0.5 4.5 3 3.5 4.5C4.3 6.2 5.8 7.7 7.5 8.5L9 7.5 11.5 9.5 10 11.5C5 11 1 7 0.5 2Z"/></svg></li>
      <li>www.rbpikehauling.example
        <svg class="icon" viewBox="0 0 12 12"><circle cx="6" cy="6" r="5.5"/><path d="M0.5 6h11M6 0.5c-3 3-3 8 0 11M6 0.5c3 3 3 8 0 11" stroke="var(--bark)" stroke-width="0.9" fill="none"/></svg></li>
      <li>rbpikehauling@mailbox.example
        <svg class="icon" viewBox="0 0 12 12"><rect x="0.5" y="2" width="11" height="8"/><path d="M0.5 2 6 6.5 11.5 2" stroke="var(--bark)" stroke-width="0.9" fill="none"/></svg></li>
      <li>PO Box 8412 Cedar Bend, Tx 77390
        <svg class="icon" viewBox="0 0 12 12"><path d="M6 0.5A4 4 0 0 1 10 4.5C10 7.5 6 11.5 6 11.5S2 7.5 2 4.5A4 4 0 0 1 6 0.5Z"/><circle cx="6" cy="4.5" r="1.5" fill="var(--bark)"/></svg></li>
    </ul>
  </div>
</section>

</body>
</html>
```